halvique TrendLens Peakdays2025

halvique Brand Background
Who We Are:
halvique is a next-generation marketing intelligence company. Our core platform, halvique TrendLens, delivers daily, real-time insights into what’s driving audience engagement and sales across 20,000+ brands and 15+ digital channels.

Mission
To empower brands and marketers to capture every revenue opportunity in an “Always-On Opportunity” economy—by transforming short-term market volatility into predictable, repeatable growth.

Vision
To make every marketing moment count. We envision a future where brands aren’t caught off-guard by trends, but are always the first to know, first to act, and always ahead of the curve—turning volatility into a strategic advantage.

Brand Claim / Tagline
halvique keeps you one step sooner, one move bolder.

Or, shorter for slides:
First to Know. First to Act.

Creative Direction / Brand Tone (optional for designers):
Modern, bold, digital-first
Data-driven and energetic
Trusted partner to ambitious, innovative brands

One-Line Summary for Designers:

“halvique empowers retail brands with real-time, actionable marketing intelligence—so you can act faster, grow smarter, and capture the opportunities others miss.”

Target Market(s)

Retail managers CEO, CMO

Industry/Entity Type

B2C Retail

Font styles to use
Sans Serif

Colors
EB3D1F
EC4F4E
F09395
F8D3D4
FCEDEE

Requirements
Must have
• Compelling brand building and selling the “Peakdays & Winterfest Sales Booster” package
Nice to have
• ^building one of the design foundations for new website design
Should not have
• unnecessary stuff, keep it clean and slim

```html
<!DOCTYPE html>
<html lang="en">
<head>
<meta charset="utf-8">
<title>halvique – Peakdays &amp; Winterfest Sales Booster</title>
<link href="https://fonts.googleapis.com/css2?family=Libre+Franklin:ital,wght@0,400;0,500;0,600;0,700;0,800;1,400;1,500&display=swap" rel="stylesheet">
<style>
:root{
  --red:#c8101a;
  --red-deep:#a50c14;
  --red-soft:#ec4f4e;
  --pink:#f09395;
  --pink-light:#f8d3d4;
  --blush:#fcedee;
  --ink:#1c1c1c;
  --text:#4a4a4a;
  --grey-band:#d9d9d9;
  --charcoal:#454b50;
  --page:#ffffff;
}
*{margin:0;padding:0;box-sizing:border-box}
html,body{width:1200px;height:2864px;overflow:hidden}
body{background:var(--page);font-family:"Libre Franklin",Arial,sans-serif;color:var(--text);position:relative}
.slide{position:absolute;left:117px;width:966px;height:544px;background:#fff;overflow:hidden;box-shadow:0 6px 18px rgba(0,0,0,.18)}
.abs{position:absolute}
.slide-title{position:absolute;left:36px;font-size:30px;font-weight:700;color:var(--charcoal);letter-spacing:-.2px}
.footer{position:absolute;left:0;bottom:0;width:100%;height:43px;background:var(--grey-band)}
.footer .brand{position:absolute;left:36px;top:9px;font-size:21px;font-weight:600;color:#555}
.footer .page{position:absolute;left:913px;top:13px;width:18px;height:18px;border-radius:50%;background:var(--red);color:#fff;font-size:10px;font-weight:600;text-align:center;line-height:18px}
.red{color:var(--red)}
b,strong{font-weight:700}

/* slide 1 */
.cover{top:14px;background:linear-gradient(100deg,#f4f4f5 0%,#eceef1 55%,#dfe5ee 100%)}
.cover .visual{left:484px;top:0;width:482px;height:470px;background:radial-gradient(ellipse at 55% 40%,#ffffff 0%,#dfe3ea 55%,#c9d0db 100%)}
.cover .logo{left:36px;top:82px;font-size:50px;font-weight:600;color:#3c3c3c;letter-spacing:-.5px}
.cover .pill{left:36px;top:243px;padding:0 12px;height:43px;line-height:43px;border-radius:22px;background:var(--red);color:#fff;font-size:17px;font-weight:500}
.cover .kicker{left:40px;top:320px;font-size:26px;color:var(--red);font-weight:500}
.cover h1{position:absolute;left:40px;top:358px;font-size:33px;line-height:1.2;font-weight:700;color:#111}
.cover .url{left:40px;top:486px;font-size:9px;color:#666}

/* slide 2 */
.about{top:587px}
.about .slide-title{top:27px}
.about .economy{left:37px;top:125px;width:258px;height:325px;border-radius:22px;background:linear-gradient(180deg,#2f4656 0%,#6b3a45 45%,#b81520 75%,#c8101a 100%);color:#fff;padding:0 20px 24px;display:flex;flex-direction:column;justify-content:flex-end;font-size:12.5px;line-height:1.45}
.about .economy h3{font-size:18px;font-weight:700;margin-bottom:2px}
.feature{position:absolute;left:353px;width:364px}
.feature .icon{position:absolute;left:0;top:-4px;width:42px;height:42px;border-radius:50%;background:var(--red)}
.feature h4{margin-left:56px;font-size:17px;font-weight:700;color:#333;margin-bottom:9px}
.feature p{margin-left:56px;font-size:13px;line-height:1.55;color:#555}
.about .rule{left:335px;width:382px;height:1px;background:#bbb}
.quote{left:713px;top:125px;width:253px;height:325px;background:var(--red);border-radius:22px 0 0 22px;color:#fff;padding:42px 24px 0 30px}
.quote .mark{font-size:34px;font-weight:800;line-height:.6;display:block;margin-bottom:12px}
.quote p{font-style:italic;font-size:13px;line-height:1.7}
.quote .by{font-size:9.5px;margin-top:14px}
.about .note{left:343px;top:454px;font-size:6.5px;color:#777}

/* slide 3 */
.summary{top:1160px}
.summary .eyebrow{left:36px;top:28px;font-size:14px;font-weight:600;color:var(--red)}
.summary .slide-title{top:52px;color:#333}
.summary .hook{left:40px;top:122px;width:344px;height:112px;background:var(--red);border-radius:10px;color:#fff;font-size:15px;line-height:1.55;padding:22px 30px}
.summary .chart{left:40px;top:246px;width:344px;height:250px;border:2px solid var(--pink-light);border-radius:12px}
.chart .label{position:absolute;font-size:10px;color:#555;line-height:1.3}
.chart .big{position:absolute;font-size:38px;font-weight:700}
.chart .big sup{font-size:20px;vertical-align:top;position:relative;top:2px}
.impact{left:431px;width:500px}
.impact .lead{font-size:15px;color:#333;line-height:1.55}
.impact ul{list-style:none;margin-top:4px}
.impact li{position:relative;padding-left:27px;font-size:15px;color:#444;line-height:29px}
.impact li::before{content:"";position:absolute;left:2px;top:12px;width:6px;height:6px;border:1.5px solid var(--red);border-radius:50%}
.circled{border:1.5px solid var(--red);border-radius:10px;padding:0 4px;color:var(--red)}
.summary .rule{left:431px;top:274px;width:470px;height:1px;background:#999}

/* slide 4 */
.attention{top:1733px}
.attention .slide-title{top:27px}
.attention .photo{left:37px;top:110px;width:309px;height:372px;border-radius:34px;background:linear-gradient(160deg,#8aa6b8 0%,#c9d3d8 45%,#8d7a6a 100%)}
.stat{position:absolute;top:133px;width:136px;height:100px;background:var(--red);border-radius:8px;color:#fff;padding:18px 16px 0}
.stat .num{font-size:34px;font-weight:700;line-height:1}
.stat .num sup{font-size:18px;vertical-align:top}
.stat .cap{font-size:13px;line-height:1.2;margin-top:4px}
.attention .check{left:393px;top:266px;width:560px;font-size:15px;line-height:1.6;color:#555}
.attention .check strong{font-size:19px;color:#333;font-weight:600}
.bolt{position:absolute;left:395px;width:560px;padding-left:27px;font-size:15px;line-height:1.55;color:#555}
.bolt svg{position:absolute;left:0;top:3px}

/* slide 5 */
.shift{top:2306px}
.shift .slide-title{top:27px}
.shift .panel{left:64px;top:142px;width:838px;height:360px;background:#fff;box-shadow:0 0 16px rgba(0,0,0,.12)}
.shift .head{position:absolute;top:102px;height:40px;color:#fff;font-size:15px;font-weight:700;text-align:center;line-height:40px;border-radius:14px 14px 0 0}
.shift .head.old{left:64px;width:418px;background:var(--charcoal)}
.shift .head.new{left:484px;width:418px;background:var(--red)}
.shift .col{position:absolute;top:142px;width:74px;height:360px}
.shift .col.old{left:349px;background:var(--charcoal)}
.shift .col.new{left:542px;background:var(--red)}
.node{position:absolute;width:32px;height:32px;border-radius:50%;background:#fff;display:flex;align-items:center;justify-content:center}
.row-old{position:absolute;left:82px;width:255px;text-align:right}
.row-new{position:absolute;left:644px;width:250px}
.row-old h5,.row-new h5{font-size:15px;font-weight:700;color:#333;margin-bottom:4px}
.row-new h5{color:var(--red)}
.row-old p,.row-new p{font-size:11px;line-height:1.55;color:#777}
.vlabel{position:absolute;font-size:13px;font-weight:500;color:#333;transform:rotate(-90deg);transform-origin:center;white-space:nowrap}
</style>
</head>
<body>

<!-- 1 · Cover -->
<section class="slide cover">
  <div class="abs visual" role="img" aria-label="Photo of a white 3D maze with a broken wall and a red ball rolling through the gap"></div>
  <div class="abs logo">halvique</div>
  <div class="abs pill">#AlwaysOnOpportunity Capture</div>
  <div class="abs kicker">Turn Market Volatility into Growth</div>
  <h1>The “Peakdays &amp; Winterfest<br>Sales Booster” package</h1>
  <div class="abs url">www.halvique.io</div>
</section>

<!-- 2 · About -->
<section class="slide about">
  <h2 class="slide-title">About halvique</h2>
  <div class="abs economy" role="img" aria-label="Photo of a digital dashboard screen with a red overlay">
    <h3>We live in an</h3>
    <p><b>#AlwaysOnOpportunity</b> economy, where market volatility is the only constant. 60% of revenue opportunities now occur outside of planned marketing campaigns.</p>
  </div>

  <div class="feature" style="top:150px">
    <span class="icon"><svg width="42" height="42" viewBox="0 0 42 42"><circle cx="21" cy="21" r="11" fill="none" stroke="#fff" stroke-width="1.6"/><text x="21" y="24" font-size="8" fill="#fff" text-anchor="middle" font-family="Arial">HOW?</text></svg></span>
    <h4>Our How:</h4>
    <p>Our AI platform <b>daily analyses 20,000+ brands</b> across 15 channels to identify what your audience is actually interested in right now.</p>
  </div>
  <div class="abs rule" style="top:241px"></div>
  <div class="feature" style="top:280px">
    <span class="icon"><svg width="42" height="42" viewBox="0 0 42 42"><rect x="13" y="11" width="16" height="20" rx="2" fill="none" stroke="#fff" stroke-width="1.6"/><path d="M16 17h10M16 21h10M16 25h6" stroke="#fff" stroke-width="1.4"/></svg></span>
    <h4>Our Claim:</h4>
    <p>halvique keeps you one step sooner, one move bolder.</p>
  </div>
  <div class="abs rule" style="top:331px"></div>
  <div class="feature" style="top:368px">
    <span class="icon"><svg width="42" height="42" viewBox="0 0 42 42"><path d="M12 26c3 4 15 4 18 0M21 12v10M16 17l5-5 5 5" fill="none" stroke="#fff" stroke-width="1.6" stroke-linecap="round"/></svg></span>
    <h4>The Result:</h4>
    <p>Brands capturing #AlwaysOnOpportunities see<br><b style="color:#333">2.8x higher revenue growth</b><sup style="font-size:7px">*)</sup></p>
  </div>
  <div class="abs note">*) Panel of 260 retail brands with revenue up to 250 mln €, August 2025.</div>

  <div class="abs quote">
    <span class="mark">“</span>
    <p>“With halvique TrendLens, we were able to spot and act on new market trends days before our competitors. The speed and clarity of insights transformed our clients’ Peakdays campaigns into true revenue drivers.”</p>
    <p class="by">Lena Marwick, CEO Brightcart</p>
  </div>
  <footer class="footer"><span class="brand">halvique</span><span class="page">2</span></footer>
</section>

<!-- 3 · Executive summary -->
<section class="slide summary">
  <div class="abs eyebrow">Executive Summary:</div>
  <h2 class="slide-title">60% of Opportunities are missed</h2>
  <div class="abs hook">Often, marketing is capturing less than 40% of potential business. <b>What if you could capture the other 60%?</b></div>
  <div class="abs chart">
    <svg class="abs" style="left:72px;top:12px" width="156" height="156" viewBox="0 0 156 156">
      <circle cx="78" cy="78" r="60" fill="none" stroke="#6e6e6e" stroke-width="26"/>
      <circle cx="78" cy="78" r="60" fill="none" stroke="var(--red)" stroke-width="26" stroke-dasharray="226 377" transform="rotate(-90 78 78)"/>
      <circle cx="78" cy="78" r="38" fill="#e4e4e4"/>
      <circle cx="78" cy="78" r="26" fill="#fff"/>
      <circle cx="78" cy="78" r="10" fill="none" stroke="#777" stroke-width="1.2"/>
      <path d="M78 62v6M78 88v6M62 78h6M88 78h6" stroke="#777" stroke-width="1.2"/>
      <polyline points="150,100 168,100" fill="none"/>
    </svg>
    <svg class="abs" style="left:0;top:0" width="344" height="250" viewBox="0 0 344 250"><path d="M170 72 L250 72 L258 92" fill="none" stroke="#666" stroke-width="1"/><path d="M100 125 L70 132 L58 160" fill="none" stroke="#666" stroke-width="1"/></svg>
    <div class="label" style="left:243px;top:97px">Unplanned<br>Opportunities:</div>
    <div class="big red" style="left:243px;top:122px">60<sup>%</sup></div>
    <div class="label" style="left:16px;top:169px">Planned Marketing:</div>
    <div class="big" style="left:16px;top:182px;color:#333">40<sup>%</sup></div>
  </div>

  <div class="abs impact" style="top:126px">
    <p class="lead">Key Business Impact of <b class="red" style="font-size:17px">#AlwaysOnOpportunity</b> capture:</p>
    <ul>
      <li>10-15% higher conversion rates</li>
      <li>15-20% increase in audience engagement</li>
      <li>20-25% higher marketing team effectiveness</li>
      <li>up to 2.8x higher revenue growth</li>
    </ul>
  </div>
  <div class="abs rule"></div>
  <div class="abs impact" style="top:300px">
    <p class="lead">Avoid the cost of inaction, get prepared for <b>Peakdays &amp; Winterfest 2025</b></p>
    <ul>
      <li>Timeline to Value: operational within 6 weeks,</li>
      <li>Investment: 2-3 of your marketing experts, <span class="circled">15.000 €</span><br>for halvique platform &amp; support,</li>
      <li>Expected results: <span class="circled">+5..10% revenue.</span></li>
    </ul>
  </div>
  <footer class="footer"><span class="brand">halvique</span><span class="page">3</span></footer>
</section>

<!-- 4 · Attention -->
<section class="slide attention">
  <h2 class="slide-title">Attention is now the #1 Line-Item Cost</h2>
  <div class="abs photo" role="img" aria-label="Photo of a marketing team planning with sticky notes on a glass wall"></div>
  <div class="stat" style="left:386px"><div class="num">3x</div><div class="cap">Costlier</div></div>
  <div class="stat" style="left:536px"><div class="num">25<sup>%</sup></div><div class="cap">Of messages<br>unread</div></div>
  <div class="stat" style="left:686px"><div class="num">80<sup>%</sup></div><div class="cap">Not ready</div></div>
  <p class="abs check"><strong>Marketing Reality Check</strong>: Attention costs are skyrocketing – Generating qualified leads at scale cost 3x more than 2020.</p>
  <p class="bolt" style="top:344px"><svg width="9" height="14" viewBox="0 0 9 14"><path d="M5 0L0 8h4l-1 6 6-9H5z" fill="#222"/></svg>Incomplete cross-channel messaging reaches only 20% of your potential Audience.</p>
  <p class="bolt" style="top:403px"><svg width="9" height="14" viewBox="0 0 9 14"><path d="M5 0L0 8h4l-1 6 6-9H5z" fill="#222"/></svg>Fragmented storytelling does not fit with current audience Interest.</p>
  <p class="bolt" style="top:437px"><svg width="9" height="14" viewBox="0 0 9 14"><path d="M5 0L0 8h4l-1 6 6-9H5z" fill="#222"/></svg>80% of audience is not in “Buy-Now” mode when your campaign hits.</p>
  <footer class="footer"><span class="brand">halvique</span><span class="page">4</span></footer>
</section>

<!-- 5 · Reactive to pro-active -->
<section class="slide shift">
  <h2 class="slide-title">From Reactive to Pro-active: turn Volatility into Growth</h2>
  <div class="abs panel"></div>
  <div class="head old">Traditional Planning</div>
  <div class="head new">Always-On Opportunity Capture</div>
  <div class="col old"></div>
  <div class="col new"></div>

  <!-- nodes -->
  <div class="node" style="left:370px;top:184px"><svg width="16" height="16" viewBox="0 0 16 16"><path d="M8 4v10M4 14h8M5 9l3-5 3 5" fill="none" stroke="#555" stroke-width="1.3"/></svg></div>
  <div class="node" style="left:370px;top:288px"><svg width="16" height="16" viewBox="0 0 16 16"><rect x="2" y="3" width="12" height="10" rx="1" fill="none" stroke="#555" stroke-width="1.3"/><path d="M5 7h6M5 10h4" stroke="#555" stroke-width="1.2"/></svg></div>
  <div class="node" style="left:370px;top:388px"><svg width="16" height="16" viewBox="0 0 16 16"><circle cx="8" cy="8" r="6" fill="none" stroke="#555" stroke-width="1.3"/><path d="M8 4v4l3 2" fill="none" stroke="#555" stroke-width="1.3"/></svg></div>
  <div class="node" style="left:563px;top:184px"><svg width="16" height="16" viewBox="0 0 16 16"><path d="M8 4v10M4 14h8M5 9l3-5 3 5" fill="none" stroke="var(--red)" stroke-width="1.3"/></svg></div>
  <div class="node" style="left:563px;top:288px"><svg width="16" height="16" viewBox="0 0 16 16"><rect x="2" y="3" width="12" height="10" rx="1" fill="none" stroke="var(--red)" stroke-width="1.3"/><path d="M5 7h6M5 10h4" stroke="var(--red)" stroke-width="1.2"/></svg></div>
  <div class="node" style="left:563px;top:388px"><svg width="16" height="16" viewBox="0 0 16 16"><circle cx="8" cy="8" r="6" fill="none" stroke="var(--red)" stroke-width="1.3"/><path d="M8 4v4l3 2" fill="none" stroke="var(--red)" stroke-width="1.3"/></svg></div>

  <!-- timeline arrows -->
  <svg class="abs" style="left:422px;top:142px" width="120" height="360" viewBox="0 0 120 360">
    <defs><linearGradient id="greyFade" x1="0" y1="0" x2="0" y2="1"><stop offset="0" stop-color="#e6e6e6"/><stop offset="1" stop-color="#444b50"/></linearGradient></defs>
    <polygon points="24,30 36,30 36,330 46,330 30,350 14,330 24,330" fill="url(#greyFade)"/>
    <polygon points="90,30 100,30 100,152 110,152 95,168 80,152 90,152" fill="var(--red)"/>
    <line x1="70" y1="176" x2="118" y2="176" stroke="var(--red)" stroke-width="1" stroke-dasharray="2 2"/>
    <polygon points="90,188 100,188 100,330 110,330 95,348 80,330 90,330" fill="var(--red)"/>
  </svg>
  <div class="vlabel" style="left:428px;top:322px">2-4 weeks</div>
  <div class="vlabel" style="left:482px;top:237px;font-size:12px">2-day fast-lane</div>
  <div class="vlabel" style="left:482px;top:400px;font-size:12px">Early Revenue</div>

  <div class="row-old" style="top:168px"><h5>Internal Signals</h5><p>Weekly tweaks to annual roadmap; few real-time signals from hypes, competitors, events. <b>Manual ex-post competitor screening.</b></p></div>
  <div class="row-old" style="top:272px"><h5>Manual Orchestration</h5><p>Break campaigns into messages by hand. Cross-channel coordination depends on complex sync and sign-of.</p></div>
  <div class="row-old" style="top:372px"><h5>Speed: Weeks</h5><p>Yearly master plan, monthly sprints, weekly refinements.</p></div>

  <div class="row-new" style="top:168px"><h5>360° Signals</h5><p>Plan + audience sentiment + trends + competitors +upcoming events. Overnight scans = fresh insight briefs by morning.</p></div>
  <div class="row-new" style="top:272px"><h5>Auto-orchestrated planning</h5><p>Campaign building and channels mapping. Daily re-calibration based on live performance.</p></div>
  <div class="row-new" style="top:372px"><h5>Speed: Days</h5><p>2-Day fast-lane activities addressing market volatility &amp; short-term opportunities. Automated 10-day / 70-day mid-term updates.</p></div>

  <footer class="footer"><span class="brand">halvique</span><span class="page">5</span></footer>
</section>

</body>
</html>
```